Wanderlark Gin - Bottle Label for a craft Gin about to be launched on the world from New Zealand

We are a start up craft distillery in New Zealand. We have developed a wonderful Gin using our own grain spirit and both traditional and New Zealand native botanicals (Manuka to be specific), chosen our bottle and the name "Wanderlark" and done a bit of amateur label design and now we are looking for someone to make it great.

Feel free to change up our amateur concept but give us something that will pop from the back bar and scream authenticity, craft and individuality.

The attached files give you the specifications of the bottle, our current concept for a Wanderlark label and an earlier concept drawing that gives an idea of where we are thinking the two labels should go on the front of the bottle.

Thanks, we look forward to your ideas!!

Target Market(s)

High end and craft Gin drinkers. Hipsters and cocktail barflys and their bar tenders and bar owners

Requirements
Must have
• Attractive individuality
Nice to have
• Coolness
Should not have
• Uncoolness

```html
<!DOCTYPE html>
<html lang="en">
<head>
<meta charset="utf-8">
<title>Wanderlark Gin – Bottle Labels</title>
<link href="https://fonts.googleapis.com/css2?family=Bebas+Neue&family=Oswald:wght@400;500;700&display=swap" rel="stylesheet">
<style>
  :root {
    --bg-top: #f4f7f9;
    --bg-bottom: #c9d8e2;
    --label-black: #0b0b0b;
    --paper-white: #ffffff;
    --accent-yellow: #f2e21a;
    --accent-green: #5bbf21;
    --art-red: #e8262a;
    --art-yellow: #f5dc1e;
    --art-magenta: #d0308f;
    --art-cyan: #27c4e6;
  }
  html, body {
    margin: 0;
    padding: 0;
    overflow: hidden;
  }
  .canvas {
    position: relative;
    width: 865px;
    height: 1200px;
    overflow: hidden;
    background: linear-gradient(180deg, var(--bg-top) 0%, var(--bg-bottom) 100%);
    font-family: "Oswald", sans-serif;
  }

  /* Front label */
  .front-label {
    position: absolute;
    left: 82px;
    top: 150px;
    width: 700px;
    height: 420px;
  }
  .front-label__shape {
    position: absolute;
    inset: 0;
  }
  .front-label__art {
    position: absolute;
    left: 80px;
    top: 30px;
    width: 540px;
    height: 290px;
    border-radius: 46% 54% 38% 62% / 48% 40% 60% 52%;
    background:
      radial-gradient(circle at 30% 25%, var(--art-yellow) 0 22%, transparent 40%),
      radial-gradient(circle at 80% 55%, var(--art-cyan) 0 18%, transparent 38%),
      radial-gradient(circle at 55% 65%, var(--art-magenta) 0 16%, transparent 36%),
      linear-gradient(120deg, var(--art-red) 0%, var(--art-magenta) 55%, var(--art-cyan) 100%);
  }
  .front-label__name {
    position: absolute;
    left: 0;
    right: 0;
    top: 110px;
    margin: 0;
    text-align: center;
    font-family: "Bebas Neue", sans-serif;
    font-size: 112px;
    font-weight: 400;
    letter-spacing: 4px;
    color: var(--paper-white);
    text-shadow: 4px 4px 0 var(--label-black);
  }
  .front-label__tagline {
    position: absolute;
    left: 0;
    right: 0;
    top: 332px;
    margin: 0;
    text-align: center;
    font-size: 20px;
    font-weight: 500;
    color: var(--paper-white);
  }
  .front-label__volume {
    position: absolute;
    left: 0;
    right: 0;
    top: 362px;
    margin: 0;
    text-align: center;
    font-size: 24px;
    font-weight: 700;
    color: var(--accent-yellow);
  }

  /* Back / lower label */
  .story-label {
    position: absolute;
    left: 122px;
    top: 820px;
    width: 620px;
    height: 300px;
    background: var(--label-black);
  }
  .story-label__badges {
    position: absolute;
    left: 0;
    right: 0;
    top: -80px;
    display: flex;
    justify-content: center;
    align-items: center;
    gap: 10px;
  }
  .badge {
    display: flex;
    flex-direction: column;
    align-items: center;
    justify-content: center;
    border-radius: 50%;
    color: var(--paper-white);
    text-align: center;
    line-height: 1;
  }
  .badge--stat {
    width: 96px;
    height: 96px;
    background: var(--label-black);
    border: 4px solid var(--paper-white);
    box-sizing: border-box;
    margin-top: 40px;
  }
  .badge--stat .badge__value {
    font-size: 32px;
    font-weight: 700;
  }
  .badge--stat .badge__unit {
    font-size: 16px;
    margin-top: 2px;
  }
  .badge--recipe {
    width: 150px;
    height: 150px;
    background: var(--accent-green);
    border: 6px solid var(--paper-white);
    box-sizing: border-box;
    box-shadow: 0 0 0 4px var(--label-black);
  }
  .badge--recipe .badge__unit {
    font-size: 24px;
    font-weight: 500;
  }
  .badge--recipe .badge__value {
    font-family: "Bebas Neue", sans-serif;
    font-size: 80px;
    margin-top: -2px;
  }
  .story-label__text {
    position: absolute;
    left: 50px;
    right: 50px;
    top: 92px;
    margin: 0;
    text-align: center;
    font-size: 22px;
    font-weight: 500;
    line-height: 1.35;
    color: var(--paper-white);
  }
  .story-label__edge {
    position: absolute;
    left: 30px;
    bottom: 14px;
    width: 560px;
    height: 30px;
  }
</style>
</head>
<body>
<main class="canvas">

  <section class="front-label">
    <svg class="front-label__shape" viewBox="0 0 700 420" width="700" height="420" aria-hidden="true">
      <polygon points="70,0 630,0 700,210 630,420 70,420 0,210" fill="var(--label-black)"/>
    </svg>
    <div class="front-label__art" role="img" aria-label="Wild cat silhouette filled with colourful botanical leaf pattern in red, yellow, magenta and cyan"></div>
    <h1 class="front-label__name">Wanderlark</h1>
    <p class="front-label__tagline">A classically inspired Gin with a New Zealand twist</p>
    <p class="front-label__volume">500ml</p>
  </section>

  <section class="story-label">
    <div class="story-label__badges">
      <div class="badge badge--stat">
        <span class="badge__value">84</span>
        <span class="badge__unit">proof</span>
      </div>
      <div class="badge badge--recipe">
        <span class="badge__unit">recipe</span>
        <span class="badge__value">#3</span>
      </div>
      <div class="badge badge--stat">
        <span class="badge__value">42%</span>
        <span class="badge__unit">vol</span>
      </div>
    </div>
    <p class="story-label__text">Distilled in-house starting with local grain and finished with 11 botanicals including a generous helping of East Coast Manuka cones, Gisborne Citrus and Otago Lavender</p>
    <svg class="story-label__edge" viewBox="0 0 560 30" width="560" height="30" aria-hidden="true">
      <polygon fill="var(--accent-green)" points="0,30 20,0 40,30 60,0 80,30 100,0 120,30 140,0 160,30 180,0 200,30 220,0 240,30 260,0 280,30 300,0 320,30 340,0 360,30 380,0 400,30 420,0 440,30 460,0 480,30 500,0 520,30 540,0 560,30"/>
    </svg>
  </section>

</main>
</body>
</html>
```